Korvi Zest inflatable water park card

had the previous design for 5 years and want to change it,
we run and own inflatable water parks
need it to be fresh, cool and professional
attached is the old design and the new QR code
the card will be giving to customer and vip customers, investors and business professional. need to have the info clear and obvious

want to receiver be wowed by the design since its not the normal corporate boring card, the logo is colorful so we can use that.

Target Market(s)

customers and professionals

Contact Information for Business Card

its all in the attachment, same information

Font styles to use
Sans Serif

Colors
34a7d8
3176b5
0455a3
eaf1f7

Requirements
Must have
• arabic name on top فيصل بن القرمزي
• phone number, email, social media link, website , quote " we are in the business of creating happy memories "
Nice to have
• QR code and blue color
• social media links
Should not have
• not clear info or too much noise

```html
<!DOCTYPE html>
<html lang="en">
<head>
<meta charset="utf-8">
<title>Korvi Zest business card</title>
<link href="https://fonts.googleapis.com/css2?family=Lato:wght@400;700;900&family=Noto+Naskh+Arabic:wght@500&display=swap" rel="stylesheet">
<style>
  :root {
    --backdrop: #2e2926;
    --card: #0d0d0e;
    --sky: #34a7d8;
    --ocean: #3176b5;
    --deep: #0455a3;
    --mist: #eaf1f7;
    --soft: #c9ced3;
    --rule: #6a6d70;
  }
  * { margin: 0; padding: 0; box-sizing: border-box; }
  html, body { width: 1200px; height: 900px; overflow: hidden; }
  body {
    background: var(--backdrop);
    position: relative;
    font-family: "Lato", Arial, sans-serif;
  }
  .card {
    position: absolute;
    width: 660px;
    height: 380px;
    background: var(--card);
    border-radius: 4px;
    box-shadow: 0 10px 30px rgba(0,0,0,.45);
    overflow: hidden;
  }
  .card--back { left: 480px; top: 50px; }
  .card--front { left: 60px; top: 470px; }

  .brand-name {
    position: absolute;
    font-family: "Lato", Arial, sans-serif;
    font-weight: 900;
    color: var(--sky);
    text-transform: uppercase;
    text-align: center;
    line-height: .95;
    letter-spacing: 2px;
  }
  .card--back .brand-name { left: 0; width: 100%; top: 70px; font-size: 58px; }
  .card--front .brand-name { left: 40px; width: 250px; top: 110px; font-size: 56px; }

  /* back */
  .rule { position: absolute; height: 1px; background: var(--rule); }
  .rule--upper { left: 370px; right: 38px; top: 188px; }
  .rule--lower { left: 118px; right: 330px; top: 305px; }
  .social {
    position: absolute; top: 222px; left: 0; width: 100%;
    display: flex; justify-content: center; gap: 6px;
  }
  .social__tile { width: 16px; height: 16px; border-radius: 2px; background: var(--ocean); }
  .social__tile:nth-child(2) { background: var(--deep); }
  .social__tile:nth-child(3) { background: var(--sky); }
  .handle {
    position: absolute; top: 244px; left: 0; width: 100%;
    text-align: center; color: var(--mist);
    font-size: 12px; font-weight: 700; letter-spacing: .5px;
  }

  /* front */
  .divider { position: absolute; left: 322px; top: 62px; width: 1px; height: 190px; background: var(--rule); }
  .contact { position: absolute; left: 348px; top: 60px; }
  .contact__arabic {
    font-family: "Noto Naskh Arabic", serif;
    color: var(--sky); font-size: 21px; font-weight: 500;
    direction: rtl; text-align: left; line-height: 1.2;
  }
  .contact__name { color: var(--sky); font-weight: 700; font-size: 19px; letter-spacing: .3px; }
  .contact__role { color: var(--soft); font-size: 15px; margin-top: 2px; }
  .contact__list { list-style: none; margin-top: 18px; }
  .contact__item {
    display: flex; align-items: center; gap: 8px;
    color: var(--mist); font-size: 15px; line-height: 24px;
  }
  .contact__icon { width: 13px; height: 13px; fill: var(--sky); flex: none; }
  .tagline {
    position: absolute; left: 0; width: 100%; top: 318px;
    text-align: center; color: var(--soft);
    font-size: 15px; letter-spacing: .6px; text-transform: uppercase;
  }
</style>
</head>
<body>

<section class="card card--back" aria-label="Card back">
  <div class="brand-name">Korvi<br>Zest</div>
  <div class="rule rule--upper"></div>
  <div class="social" aria-label="Social profiles">
    <span class="social__tile"></span>
    <span class="social__tile"></span>
    <span class="social__tile"></span>
  </div>
  <div class="handle">KORVIZESTME</div>
  <div class="rule rule--lower"></div>
</section>

<section class="card card--front" aria-label="Card front">
  <div class="brand-name">Korvi<br>Zest</div>
  <div class="divider"></div>
  <div class="contact">
    <p class="contact__arabic" lang="ar">فيصل بن القرمزي</p>
    <p class="contact__name">FAISAL BEN ALQIRMIZI</p>
    <p class="contact__role">Founder - CEO</p>
    <ul class="contact__list">
      <li class="contact__item">
        <svg class="contact__icon" viewBox="0 0 16 16"><path d="M3.5 1l3 3-1.6 2a9 9 0 0 0 5.1 5.1l2-1.6 3 3-2 2.5C6.5 14.5 1.5 9.5 1 3z"/></svg>
        +971 50 316 2047
      </li>
      <li class="contact__item">
        <svg class="contact__icon" viewBox="0 0 16 16"><path d="M1 3h14v10H1z M1.5 3.5L8 9l6.5-5.5" stroke="#0d0d0e" stroke-width="1.2"/></svg>
        faisal@korvizest.ae
      </li>
      <li class="contact__item">
        <svg class="contact__icon" viewBox="0 0 16 16"><circle cx="8" cy="8" r="7"/><path d="M1 8h14M8 1c-3 3.5-3 10.5 0 14M8 1c3 3.5 3 10.5 0 14" stroke="#0d0d0e" stroke-width="1" fill="none"/></svg>
        www.korvizest.ae
      </li>
    </ul>
  </div>
  <p class="tagline">We are in the business of creating happy memories</p>
</section>

</body>
</html>
```